Redesign of Bright Harbor Entertainment Card

I already have my logo and font design for my company name. I am looking to come up with a Unique way of having it on my business card. Just looking for a really hip, and professional business card while still using my logo design.

I have also enclosed the front and back of the card so you can see what I have now. Looking for something different.

Thank you!

Target Market(s)

Young to middle aged brides and grooms

Industry/Entity Type

Business

Requirements
Should not have
• Cheese

```html
<!DOCTYPE html>
<html lang="en">
<head>
<meta charset="utf-8">
<title>Bright Harbor Entertainment – Business Card</title>
<link rel="stylesheet" href="https://fonts.googleapis.com/css2?family=Montserrat:wght@500;700;800&family=Open+Sans:wght@400;600;700&display=swap">
<style>
  :root {
    --backdrop: #e9e6e2;
    --card: #ffffff;
    --brand-deep: #3b2fb0;
    --brand-blue: #2f6fd6;
    --brand-sky: #29a8e6;
    --text-dark: #4a4a4a;
    --text-mid: #5a5a5a;
    --icon: #3a6fc9;
    --band-start: #2f5fd0;
    --band-end: #3a7fe0;
    --band-text: #ffffff;
  }
  * { box-sizing: border-box; margin: 0; padding: 0; }
  html, body { width: 1200px; height: 970px; overflow: hidden; }
  body {
    background: var(--backdrop);
    font-family: "Open Sans", Arial, sans-serif;
    position: relative;
  }
  .card {
    position: absolute;
    left: 100px; top: 207px;
    width: 1000px; height: 556px;
    background: var(--card);
    border-radius: 40px;
    overflow: hidden;
    box-shadow: 0 10px 30px rgba(0,0,0,0.15);
  }
  .brand {
    position: absolute;
    left: 96px; top: 38px;
    display: flex; align-items: center; gap: 24px;
  }
  .brand-dot {
    width: 140px; height: 140px; border-radius: 50%;
    background: radial-gradient(circle at 45% 40%, var(--brand-sky), var(--brand-blue));
  }
  .brand-text { display: flex; flex-direction: column; }
  .brand-name {
    font-family: "Montserrat", Arial, sans-serif;
    font-weight: 800;
    font-size: 58px;
    line-height: 1.02;
    letter-spacing: 4px;
    color: var(--brand-deep);
    text-transform: uppercase;
  }
  .brand-tagline {
    font-family: "Montserrat", Arial, sans-serif;
    font-weight: 500;
    font-size: 13.5px;
    letter-spacing: 0.6px;
    color: var(--brand-blue);
    text-transform: uppercase;
    margin-top: 6px;
  }
  .person { position: absolute; left: 96px; top: 222px; }
  .person-name {
    font-family: "Open Sans", Arial, sans-serif;
    font-weight: 700; font-size: 34px; color: var(--text-dark);
  }
  .person-role { font-size: 23px; color: var(--text-mid); margin-top: 2px; }
  .contacts {
    position: absolute; left: 96px; top: 324px;
    list-style: none;
  }
  .contacts li {
    display: flex; align-items: center; gap: 24px;
    height: 39px; font-size: 20px; color: var(--text-mid);
  }
  .contacts svg { width: 26px; height: 26px; flex: none; }
  .social-box { width: 24px; height: 24px; background: var(--icon); border-radius: 3px; flex: none; margin: 0 1px; }
  .accent-disc {
    position: absolute;
    right: -120px; top: 170px;
    width: 390px; height: 390px; border-radius: 50%;
    background: linear-gradient(160deg, var(--brand-sky), var(--brand-blue));
    opacity: 0.9;
  }
  .services {
    position: absolute; left: 0; bottom: 0;
    width: 100%; height: 76px;
    background: linear-gradient(90deg, var(--band-start), var(--band-end));
    display: flex; align-items: center;
    padding-left: 36px; gap: 12px;
    color: var(--band-text);
    font-weight: 700; font-size: 22px;
  }
  .services .sep { font-size: 16px; }
</style>
</head>
<body>
  <main class="card">
    <div class="accent-disc" aria-hidden="true"></div>

    <header class="brand">
      <div class="brand-dot" aria-hidden="true"></div>
      <div class="brand-text">
        <span class="brand-name">Bright Harbor</span>
        <span class="brand-tagline">Entertainment &amp; Event Professionals</span>
      </div>
    </header>

    <section class="person">
      <h1 class="person-name">Evan Marlowe</h1>
      <p class="person-role">Owner/DJ/Emcee</p>
    </section>

    <ul class="contacts">
      <li>
        <svg viewBox="0 0 24 24" aria-hidden="true"><path fill="var(--icon)" d="M3 9c0-3 4-5 9-5s9 2 9 5v1h-4V8c-1-.6-3-1-5-1s-4 .4-5 1v2H3zM7 11h10l3 8H4z"/><circle cx="12" cy="15" r="2.2" fill="#fff"/></svg>
        <span>617-555-BEAT (2328)</span>
      </li>
      <li>
        <svg viewBox="0 0 24 24" aria-hidden="true"><rect x="2.5" y="5" width="19" height="14" fill="none" stroke="var(--icon)" stroke-width="2"/><path d="M3 6l9 7 9-7" fill="none" stroke="var(--icon)" stroke-width="2"/></svg>
        <span>info@brightharborent.com</span>
      </li>
      <li>
        <svg viewBox="0 0 24 24" aria-hidden="true"><circle cx="12" cy="12" r="9.5" fill="none" stroke="var(--icon)" stroke-width="2"/><path d="M2.5 12h19M12 2.5c-4 5-4 14 0 19M12 2.5c4 5 4 14 0 19" fill="none" stroke="var(--icon)" stroke-width="1.6"/></svg>
        <span>brightharborent.com</span>
      </li>
      <li>
        <span class="social-box" aria-hidden="true"></span>
        <span>social: @brightharborentertainment</span>
      </li>
    </ul>

    <footer class="services">
      <span>DJs/Emcees</span><span class="sep">•</span>
      <span>Lighting</span><span class="sep">•</span>
      <span>Wireless LED Uplighting</span><span class="sep">•</span>
      <span>Photo Booths</span>
    </footer>
  </main>
</body>
</html>
```